Corvanta512 Business Card Redesign

I want to create a design for brand new business cards, I need something exceptional for clear plastic business card design. Please do not submit without it being on a clear design. Photos of the various logo versions attached.

```html
<!DOCTYPE html>
<html lang="en">
<head>
<meta charset="utf-8">
<title>Corvanta512 Business Card</title>
<link href="https://fonts.googleapis.com/css2?family=Montserrat:wght@400;600;700&display=swap" rel="stylesheet">
<style>
  :root {
    --backdrop: #2b2b2d;
    --navy: #22305a;
    --gold: #c9a55a;
    --gold-light: #e6cb8a;
    --clear: rgba(120, 122, 128, 0.55);
    --clear-edge: rgba(255, 255, 255, 0.18);
    --ink-light: #eef0f5;
  }
  html, body {
    margin: 0;
    width: 1200px;
    height: 873px;
    overflow: hidden;
    background: var(--backdrop);
    font-family: "Montserrat", sans-serif;
  }
  .card {
    position: absolute;
    left: 180px;
    top: 196px;
    width: 840px;
    height: 480px;
    border-radius: 34px;
    overflow: hidden;
    background: var(--clear);
    box-shadow: inset 0 0 0 2px var(--clear-edge), 0 18px 40px rgba(0,0,0,0.45);
  }
  .card-shapes {
    position: absolute;
    inset: 0;
  }
  .contact-block {
    position: absolute;
    left: 62px;
    top: 104px;
    color: var(--ink-light);
  }
  .full-name {
    margin: 0;
    font-size: 40px;
    font-weight: 700;
    letter-spacing: 1px;
    color: var(--gold);
    line-height: 1;
  }
  .job-title {
    margin: 6px 0 26px;
    font-size: 24px;
    font-weight: 400;
    letter-spacing: 1px;
    line-height: 1;
  }
  .contact-list {
    list-style: none;
    margin: 0;
    padding: 0;
  }
  .contact-item {
    display: flex;
    align-items: center;
    gap: 14px;
    font-size: 23px;
    font-weight: 400;
    letter-spacing: 0.5px;
    margin-bottom: 12px;
  }
  .contact-icon {
    width: 24px;
    height: 24px;
    flex: none;
  }
  .brand {
    position: absolute;
    left: 500px;
    top: 200px;
    width: 300px;
    display: flex;
    flex-direction: column;
    align-items: center;
    gap: 22px;
  }
  .brand-dot {
    width: 92px;
    height: 92px;
    border-radius: 50%;
    background: var(--gold);
  }
  .brand-name {
    font-size: 40px;
    font-weight: 700;
    color: var(--gold);
    letter-spacing: 1px;
  }
</style>
</head>
<body>
  <div class="card">
    <svg class="card-shapes" viewBox="0 0 840 480" width="840" height="480">
      <path class="navy-panel" d="M0 0 H478 C392 110 338 260 352 480 H0 Z" fill="var(--navy)"/>
      <path class="gold-arc" d="M484 0 H520 C420 110 360 260 372 480 H360 C340 270 392 118 484 0 Z" fill="var(--gold)"/>
    </svg>

    <div class="contact-block">
      <h1 class="full-name">FULL NAME</h1>
      <p class="job-title">TITLE</p>
      <ul class="contact-list">
        <li class="contact-item">
          <svg class="contact-icon" viewBox="0 0 24 24"><path d="M6.6 2.5 9.4 6.4 7.6 8.6c1 2.4 3.2 4.8 5.8 5.9l2.1-1.8 3.9 2.8-1.6 3.6C9.8 19.2 3.6 12.4 3 4.2Z" fill="var(--gold)"/></svg>
          <span>(000) 000 0000</span>
        </li>
        <li class="contact-item">
          <svg class="contact-icon" viewBox="0 0 24 24" fill="none" stroke="var(--gold)" stroke-width="1.8"><circle cx="12" cy="12" r="10"/><ellipse cx="12" cy="12" rx="4.5" ry="10"/><path d="M2 12h20M4 7h16M4 17h16"/></svg>
          <span>www.company.com</span>
        </li>
        <li class="contact-item">
          <svg class="contact-icon" viewBox="0 0 24 24"><path d="M1 5h22v14H1Z" fill="var(--gold)"/><path d="M1 5l11 8 11-8M1 19l8-7M23 19l-8-7" fill="none" stroke="var(--navy)" stroke-width="1.5"/></svg>
          <span>email@company.com</span>
        </li>
      </ul>
    </div>

    <div class="brand">
      <div class="brand-dot"></div>
      <div class="brand-name">Corvanta512</div>
    </div>
  </div>
</body>
</html>
```